WEB PAGES DESIGN

We need a web design for a new company called "NUBRA42". Our major business is that provide Internet Data Center solution, such as: rack/colocation, bandwidth, dedicated server, cloud server, CDN, and so on.
Requirements of Design:
1. Home page layout can refer to index-content.jpg in the attachments, but not limited.
2. According to match logo colors to design colors of web pages, Logo in the attachments.
3. The web contents of home page in image of the index-content.jpg.
4. The successful bidder will need to design three banner.
Industry/Entity Type
Business

```html
<!DOCTYPE html>
<html lang="en">
<head>
<meta charset="utf-8">
<title>NUBRA42 — IDC Solutions</title>
<link href="https://fonts.googleapis.com/css2?family=Bree+Serif&family=Montserrat:wght@400;600;700&family=Open+Sans:ital,wght@0,400;0,600;1,400;1,600&display=swap" rel="stylesheet">
<style>
  :root{
    --green:#7cc242;
    --yellow:#f5c518;
    --orange:#f0a830;
    --navy:#262b4f;
    --ink:#2b2f3a;
    --muted:#777a80;
    --cream:#f7f3ec;
    --footer:#4a4a4c;
    --white:#ffffff;
  }
  *{box-sizing:border-box;margin:0;padding:0}
  html,body{width:1200px;height:2520px;overflow:hidden}
  body{font-family:"Open Sans",sans-serif;color:var(--ink);background:var(--white);position:relative}

  /* header */
  .site-header{position:absolute;top:0;left:0;width:1200px;height:132px;background:var(--white)}
  .brand{display:flex;align-items:center;gap:12px;font-family:"Montserrat",sans-serif;font-weight:700;font-size:30px;color:var(--green);white-space:nowrap}
  .site-header .brand{position:absolute;left:90px;top:46px}
  .brand-mark{width:26px;height:26px;background:var(--green);flex:none}
  .main-nav{position:absolute;left:300px;top:54px;display:flex;gap:28px;font-family:"Montserrat",sans-serif;font-size:12px;font-weight:600;color:var(--ink);white-space:nowrap}
  .main-nav a{color:inherit;text-decoration:none;padding-bottom:6px}
  .main-nav a.active{color:var(--green);border-bottom:2px solid var(--green)}
  .header-help{position:absolute;left:860px;top:28px;width:250px;white-space:nowrap}
  .header-help p{font-size:11px;color:var(--muted);margin-bottom:12px}
  .help-row{display:flex;align-items:center;justify-content:space-between}
  .btn-chat{background:var(--green);color:var(--white);font-size:13px;font-weight:600;padding:7px 20px;border-radius:3px}
  .phone{font-family:"Montserrat",sans-serif;font-size:24px;font-weight:600}

  /* hero */
  .hero{position:absolute;top:132px;left:0;width:1200px;height:688px}
  .hero-photo{position:absolute;inset:0;background:linear-gradient(120deg,#c9d9e4 0%,#e8d7b0 45%,#b8a07a 70%,#5b4a3a 100%)}
  .hero-content{position:absolute;left:268px;top:200px;color:var(--white)}
  .hero-title{font-family:"Bree Serif",serif;font-size:58px;letter-spacing:1px;line-height:1.1}
  .hero-lead{font-style:italic;font-weight:600;font-size:25px;line-height:1.3;width:680px;margin-top:10px;color:#fff8e1}
  .hero-icon{position:absolute;left:570px;top:370px}
  .domain-search{position:absolute;left:368px;top:500px;display:flex;height:60px;box-shadow:0 2px 6px rgba(0,0,0,.15)}
  .domain-input{width:240px;background:var(--white);font-size:17px;color:#666;display:flex;align-items:center;padding-left:22px}
  .domain-tld{width:96px;background:var(--yellow);font-size:17px;font-weight:600;display:flex;align-items:center;justify-content:center}
  .domain-btn{width:130px;background:var(--green);color:var(--white);font-size:14px;font-weight:600;display:flex;align-items:center;justify-content:center;white-space:nowrap}

  /* products */
  .products{position:absolute;top:820px;left:0;width:1200px;height:620px;background:var(--cream);text-align:center}
  .section-title{font-family:"Montserrat",sans-serif;font-weight:700;font-size:44px;color:var(--ink);padding-top:68px}
  .section-sub{font-size:18px;color:#444;margin-top:6px}
  .product-grid{position:absolute;top:218px;left:100px;width:1000px;display:flex;justify-content:space-between}
  .product{width:230px;text-align:center}
  .product-icon{width:108px;height:108px;border-radius:50%;margin:0 auto}
  .product-icon.rack{background:var(--yellow)}
  .product-icon.reseller{background:#9fd4ea}
  .product-icon.dedicated{background:#6bb5d8}
  .product-icon.hosting{background:#2eb39b}
  .product-rule{width:56px;height:2px;background:#cfcac0;margin:30px auto 20px}
  .product h3{font-weight:600;font-size:24px;color:var(--orange);white-space:nowrap}
  .product p{font-size:13px;line-height:1.55;color:#555;margin-top:18px}

  /* partners */
  .partners{position:absolute;top:1440px;left:0;width:1200px;height:288px;background:var(--white)}
  .partners-intro{position:absolute;left:90px;top:68px;width:300px}
  .partners-intro h2{font-family:"Montserrat",sans-serif;font-weight:700;font-size:34px;color:var(--navy)}
  .partners-intro p{font-size:13px;color:var(--muted);line-height:1.5;margin-top:10px}
  .partner-list{position:absolute;left:440px;top:84px;display:flex;gap:36px}
  .partner{width:150px;height:104px;border:1px solid #e6e6e6;background:#fafafa;display:flex;align-items:center;justify-content:center}
  .partner span{display:block;width:50px;height:50px;background:#d6d8dc}

  /* news */
  .news{position:absolute;top:1728px;left:0;width:1200px;height:232px;background:var(--navy);color:var(--white)}
  .news h2{position:absolute;left:180px;top:48px;font-family:"Montserrat",sans-serif;font-weight:600;font-size:34px}
  .news ul{position:absolute;left:180px;top:102px;list-style:none;font-size:14px;line-height:1.55;color:#c3c6d8}
  .btn-more{position:absolute;left:820px;top:60px;width:200px;height:92px;background:var(--green);color:var(--white);font-size:18px;font-weight:600;display:flex;align-items:center;justify-content:center}

  /* footer */
  .site-footer{position:absolute;top:1960px;left:0;width:1200px;height:560px;background:var(--footer);color:var(--white)}
  .world-map{position:absolute;left:80px;top:80px;width:860px;height:350px;background:radial-gradient(ellipse at center,rgba(255,255,255,.13) 0%,rgba(255,255,255,.06) 45%,rgba(255,255,255,0) 72%)}
  .map-pin{position:absolute;left:620px;top:282px;display:flex;align-items:center;gap:14px;font-size:16px;font-weight:600}
  .contact{position:absolute;right:90px;top:118px;text-align:right;font-size:14px;line-height:1.8;color:#e4e4e4}
  .contact h4{font-size:18px;font-weight:600;color:var(--white);margin-bottom:8px}
  .social{position:absolute;right:90px;top:340px;display:flex;gap:12px}
  .social span{width:18px;height:18px;border-radius:50%;background:var(--yellow)}
  .back-top{position:absolute;right:90px;top:408px;font-size:13px;color:#ddd}
  .copyright{position:absolute;left:0;width:1200px;top:480px;display:flex;justify-content:center;align-items:center;gap:18px;font-size:13px;color:#ddd}
  .copyright .brand{font-size:24px}
  .copyright .brand-mark{width:22px;height:22px}
</style>
</head>
<body>

<header class="site-header">
  <div class="brand"><span class="brand-mark"></span>NUBRA42</div>
  <nav class="main-nav">
    <a class="active" href="#">HOME</a>
    <a href="#">DEDICATED SERVERS</a>
    <a href="#">HOSTING</a>
    <a href="#">DATA CENTERS</a>
    <a href="#">ABOUT US</a>
  </nav>
  <div class="header-help">
    <p>Need help? Talk to our team now or call us</p>
    <div class="help-row"><span class="btn-chat">Live Chat</span><span class="phone">0000-0000</span></div>
  </div>
</header>

<section class="hero">
  <div class="hero-photo" role="img" aria-label="Photo of a hot air balloon rising against a hazy sky above trees"></div>
  <div class="hero-content">
    <h1 class="hero-title">IDC Solutions</h1>
    <p class="hero-lead">NUBRA42 Provides a wide range of highly specialized solutions that utilizes technology to transform your organization.</p>
  </div>
  <svg class="hero-icon" width="80" height="72" viewBox="0 0 80 72" aria-hidden="true">
    <g fill="none" stroke="#ffffff" stroke-width="3">
      <line x1="40" y1="14" x2="16" y2="56"/><line x1="40" y1="14" x2="64" y2="56"/><line x1="16" y1="56" x2="64" y2="56"/>
      <circle cx="40" cy="12" r="9" fill="#d9c9a6"/><circle cx="14" cy="58" r="9" fill="#d9c9a6"/><circle cx="66" cy="58" r="9" fill="#d9c9a6"/>
    </g>
  </svg>
  <div class="domain-search">
    <div class="domain-input">Your Domain Name ...</div>
    <div class="domain-tld">.com</div>
    <div class="domain-btn">Check Availability</div>
  </div>
</section>

<section class="products">
  <h2 class="section-title">Our Products</h2>
  <p class="section-sub">Our Best Features</p>
  <div class="product-grid">
    <div class="product">
      <div class="product-icon rack" role="img" aria-label="Icon of a support agent"></div>
      <div class="product-rule"></div>
      <h3>Rack &amp; Bandwidth</h3>
      <p>Secure rack space with steady power and fast links ready for your servers.</p>
    </div>
    <div class="product">
      <div class="product-icon reseller" role="img" aria-label="Icon of a cloud"></div>
      <div class="product-rule"></div>
      <h3>Reseller &amp; Referral</h3>
      <p>Grow with our partner plans and earn rewards for every client you refer.</p>
    </div>
    <div class="product">
      <div class="product-icon dedicated" role="img" aria-label="Icon of a team group"></div>
      <div class="product-rule"></div>
      <h3>Dedicated Servers</h3>
      <p>Full machines built for you with root access and round the clock care.</p>
    </div>
    <div class="product">
      <div class="product-icon hosting" role="img" aria-label="Icon of a monitor with a chart"></div>
      <div class="product-rule"></div>
      <h3>Servers Hosting</h3>
      <p>Flexible hosting that scales with demand and keeps your sites online fast.</p>
    </div>
  </div>
</section>

<section class="partners">
  <div class="partners-intro">
    <h2>Our Partners</h2>
    <p>We work with trusted network, hardware and software partners to bring you reliable service every day.</p>
  </div>
  <div class="partner-list">
    <div class="partner"><span></span></div>
    <div class="partner"><span></span></div>
    <div class="partner"><span></span></div>
    <div class="partner"><span></span></div>
  </div>
</section>

<section class="news">
  <h2>Latest News</h2>
  <ul><li>News 1</li><li>News 2</li><li>News 3</li><li>News 4</li></ul>
  <div class="btn-more">More Details</div>
</section>

<footer class="site-footer">
  <div class="world-map" role="img" aria-label="Faint world map"></div>
  <div class="map-pin">
    <svg width="28" height="38" viewBox="0 0 28 38" aria-hidden="true"><path d="M14 0C6 0 0 6 0 14c0 10 14 24 14 24s14-14 14-24C28 6 22 0 14 0z" fill="#f5c518"/><circle cx="14" cy="14" r="5" fill="#4a4a4c"/></svg>
    abc location
  </div>
  <div class="contact">
    <h4>Contact Details</h4>
    <p>Address: abc 123</p>
    <p>Phone: 000-000-000</p>
    <p>Fax: 000-000-000</p>
    <p>Email: info@nubra42.com</p>
    <p>Website: www.nubra42.com</p>
  </div>
  <div class="social"><span></span><span></span><span></span></div>
  <div class="back-top">Back To Top</div>
  <div class="copyright">Copyright © 2015 NUBRA42 <span class="brand"><span class="brand-mark"></span>NUBRA42</span></div>
</footer>

</body>
</html>
```